Marcus Lindqvist Photography needs a business card designs

I am looking for a business card with a logo clean and simple which I can use that logo on my website or on my pictures. It has to be very classy and very professional. Please look at my website at www.marcuslvqphoto.com for my signature. I'm thinking of something like that for my signature/logo. I'm still working on my website but you get an idea. I'm open to any design but not too busy graphics.

I will be printing the business card from qrivel.com.

Surprise me :)

contact me if you have any questions.

-ML

I'm receiving a lot of black background at the moment. I know my website is all black doesn't mean I want my card to be all black. Please send in with some white background as well. Thanks :)

check out some business cards that I found online. I think they are simple and look really awesome. I don't want a card that is too busy.

http://www.marcuslvqphoto.com/p270092084

Reason: Please extend the date for me. I haven't really receive any good design yet.

Printing

• -a logo that related to my first and last initial of my name "ML"
-double sided
• -I don't want my background to be all black.
-no pictures on the card

```html
<!DOCTYPE html>
<html lang="en">
<head>
<meta charset="utf-8">
<title>Marcus Lindqvist Photography – Business Card</title>
<link rel="stylesheet" href="https://fonts.googleapis.com/css2?family=Open+Sans:wght@400;600;700&display=swap">
<style>
  :root {
    --stage-light: #94cc18;
    --stage-dark: #7bb30a;
    --card-white: #ffffff;
    --card-black: #0b0b0b;
    --card-black-glow: #2a2a2a;
    --brand-red: #c8262b;
    --ink: #2b2b2b;
    --ink-soft: #3a3a3a;
    --label: #ffffff;
  }
  * { margin: 0; padding: 0; box-sizing: border-box; }
  html, body { width: 884px; height: 1200px; overflow: hidden; }
  body {
    position: relative;
    font-family: "Open Sans", Arial, sans-serif;
    background: radial-gradient(ellipse at 50% 50%, var(--stage-light) 0%, var(--stage-dark) 75%);
  }
  .card {
    position: absolute;
    left: 106px;
    width: 676px;
    height: 438px;
  }
  .card--front { top: 125px; background: var(--card-white); }
  .card--back {
    top: 661px;
    background: radial-gradient(ellipse 70% 60% at 50% 30%, var(--card-black-glow) 0%, var(--card-black) 85%);
  }
  .side-label {
    position: absolute;
    left: 0; width: 884px;
    text-align: center;
    color: var(--label);
    font-size: 19px;
    font-weight: 400;
  }
  .side-label--front { top: 587px; }
  .side-label--back { top: 1118px; }

  .brand {
    position: absolute;
    display: flex;
    flex-direction: column;
    align-items: center;
    color: var(--brand-red);
    font-weight: 700;
    text-align: center;
  }
  .brand__square {
    width: 56px; height: 56px;
    background: var(--brand-red);
    margin-bottom: 16px;
  }
  .brand__name { font-size: 21px; letter-spacing: 0.5px; line-height: 1.2; }
  .brand__trade { font-size: 12px; letter-spacing: 5px; margin-top: 8px; }

  .card--front .brand { left: 60px; top: 145px; width: 226px; }
  .card--back .brand { left: 440px; top: 245px; width: 190px; }
  .card--back .brand__square { width: 44px; height: 44px; margin-bottom: 12px; }
  .card--back .brand__name { font-size: 18px; }
  .card--back .brand__trade { font-size: 10px; letter-spacing: 4px; }

  .contact {
    position: absolute;
    left: 333px;
    top: 128px;
    color: var(--ink-soft);
  }
  .contact__name {
    color: var(--brand-red);
    font-size: 32px;
    font-weight: 600;
    letter-spacing: 2px;
    line-height: 1;
  }
  .contact__role {
    color: var(--ink);
    font-size: 20px;
    font-weight: 600;
    margin-top: 9px;
  }
  .contact__list { list-style: none; margin-top: 29px; font-size: 18px; line-height: 24.5px; }
  .contact__key { color: var(--brand-red); font-weight: 600; }
</style>
</head>
<body>
  <section class="card card--front" aria-label="Card front">
    <div class="brand">
      <div class="brand__square"></div>
      <div class="brand__name">MARCUS LINDQVIST</div>
      <div class="brand__trade">PHOTOGRAPHY</div>
    </div>
    <div class="contact">
      <h1 class="contact__name">YOUR NAME</h1>
      <p class="contact__role">Photographer</p>
      <ul class="contact__list">
        <li>your office address</li>
        <li><span class="contact__key">website</span> www.yoursite.com</li>
        <li><span class="contact__key">email</span> your_mail@yoursite.com</li>
        <li><span class="contact__key">phone</span> 081 123 456 789</li>
      </ul>
    </div>
  </section>
  <p class="side-label side-label--front">FRONT</p>

  <section class="card card--back" aria-label="Card back">
    <div class="brand">
      <div class="brand__square"></div>
      <div class="brand__name">MARCUS LINDQVIST</div>
      <div class="brand__trade">PHOTOGRAPHY</div>
    </div>
  </section>
  <p class="side-label side-label--back">BACK</p>
</body>
</html>
```